Book Cover "Venice"

Creation of a cover (14 x 20.5 cm + bleed area) for a book:
Image: “BrumeVerte” (Tiff joined)
AUTHOR: Corinne Valmer
TITLE: The murmurs of Lorient
PUBLISHER: Editions Pluvane (AT THE BOTTOM OF THE COVER)

Target Market(s)

Readers of romantic novels

Industry/Entity Type

Book

```html
<!DOCTYPE html>
<html lang="en">
<head>
<meta charset="utf-8">
<title>The murmurs of Lorient — Corinne Valmer</title>
<link rel="stylesheet" href="https://fonts.googleapis.com/css2?family=Crimson+Text&family=Alegreya+Sans:ital,wght@1,400&family=Nunito:wght@300&display=swap">
<style>
  :root {
    --page: #ffffff;
    --sky-top: #e8401f;
    --sky-mid: #d92a12;
    --sky-low: #8a1a10;
    --night: #1c0e10;
    --ink-light: #ffffff;
  }
  html, body {
    margin: 0;
    width: 1200px;
    height: 1200px;
    overflow: hidden;
    background: var(--page);
  }
  .stage {
    position: relative;
    width: 1200px;
    height: 1200px;
  }
  .cover {
    position: absolute;
    left: 258px;
    top: 100px;
    width: 683px;
    height: 1000px;
    overflow: hidden;
  }
  .cover-art {
    position: absolute;
    inset: 0;
    background:
      radial-gradient(ellipse 70% 40% at 60% 30%, rgba(240,80,40,0.35), transparent 70%),
      linear-gradient(180deg, var(--sky-top) 0%, var(--sky-mid) 38%, var(--sky-low) 62%, var(--night) 80%, var(--night) 100%);
  }
  .author {
    position: absolute;
    top: 70px;
    left: 0;
    right: 0;
    margin: 0;
    text-align: center;
    font-family: "Crimson Text", serif;
    font-weight: 400;
    font-size: 40px;
    line-height: 60px;
    letter-spacing: 0.32em;
    text-transform: uppercase;
    color: var(--ink-light);
  }
  .author span { display: block; padding-left: 0.32em; }
  .title {
    position: absolute;
    right: 120px;
    top: 660px;
    margin: 0;
    text-align: right;
    font-family: "Alegreya Sans", sans-serif;
    font-style: italic;
    font-weight: 400;
    font-size: 82px;
    line-height: 92px;
    color: var(--ink-light);
    text-shadow: 0 2px 6px rgba(0,0,0,0.45);
  }
  .title span { display: block; }
  .publisher {
    position: absolute;
    bottom: 36px;
    left: 0;
    right: 0;
    margin: 0;
    text-align: center;
    font-family: "Nunito", sans-serif;
    font-weight: 300;
    font-size: 24px;
    color: var(--ink-light);
  }
</style>
</head>
<body>
  <main class="stage">
    <article class="cover">
      <div class="cover-art" role="img" aria-label="Photograph by BrumeVerte: silhouette of a domed church and lit street lanterns against a blazing red sunset sky"></div>
      <h2 class="author"><span>Corinne</span><span>Valmer</span></h2>
      <h1 class="title"><span>The murmurs</span><span>of Lorient</span></h1>
      <p class="publisher">Editions Pluvane</p>
    </article>
  </main>
</body>
</html>
```